Medical Billing - Professional Marketing Flier

We are needing help designing a clean and professional looking easy to read marketing flier for a medical billing practice. The text needs to be large enough to print. We are looking for a 5.5 x 8.5 design that we can edit the text as needed. I have included our logo and what we initially want it to say. Please keep in mind, we also want our logo and contact details on the flier. Let me know if you have any questions.

```html
<!DOCTYPE html>
<html lang="en">
<head>
<meta charset="utf-8">
<title>Vega Billing – Flier</title>
<link href="https://fonts.googleapis.com/css2?family=Crimson+Text:wght@400;600&display=swap" rel="stylesheet">
<style>
  :root {
    --backdrop: #efe3d5;
    --paper: #ffffff;
    --ink: #3b3a3c;
    --brand: #8a5aa8;
    --billing-band: #c4609e;
    --billing-bg: #f3e6ef;
    --aging-band: #7060a6;
    --aging-bg: #e8e4ee;
    --cred-band: #1a7cc0;
    --cred-bg: #dce9f3;
    --contact-band: #1c55a0;
    --contact-bg: #dfe4ef;
  }
  * { margin: 0; padding: 0; box-sizing: border-box; }
  html, body {
    width: 999px; height: 1200px; overflow: hidden;
    background: var(--backdrop);
    font-family: "Crimson Text", Georgia, serif;
    color: var(--ink);
  }
  .flier {
    position: absolute;
    left: 118px; top: 10px;
    width: 764px; height: 1180px;
    background: var(--paper);
  }
  .header { position: absolute; left: 0; top: 0; width: 100%; height: 143px; }
  .brand {
    position: absolute; left: 66px; top: 52px;
    display: flex; align-items: center; gap: 10px;
    font-size: 34px; font-weight: 600; letter-spacing: 1px;
    color: var(--brand);
  }
  .brand-dot { width: 26px; height: 26px; border-radius: 50%; background: var(--brand); }
  .contact {
    position: absolute; right: 58px; top: 48px;
    text-align: right; font-size: 15.5px; line-height: 21px;
  }
  .contact-rule {
    position: absolute; right: 58px; top: 46px;
    width: 78px; height: 1px; background: var(--ink);
  }
  .section {
    position: absolute; left: 0; width: 100%; height: 253px;
  }
  .section .band {
    position: absolute; left: 0; top: 0; width: 66px; height: 100%;
  }
  .section .label {
    position: absolute; left: 33px; top: 50%;
    transform: translate(-50%, -50%) rotate(-90deg);
    white-space: nowrap;
    color: #fff; font-size: 25px; letter-spacing: 0.5px;
  }
  .section .copy {
    position: absolute; left: 88px; right: 48px; top: 50%;
    transform: translateY(-50%);
    font-size: 19.6px; line-height: 25.5px;
    text-align: justify; hyphens: auto;
  }
  .billing { top: 143px; background: var(--billing-bg); }
  .billing .band { background: var(--billing-band); }
  .aging { top: 405px; background: var(--aging-bg); }
  .aging .band { background: var(--aging-band); }
  .credentialing { top: 667px; background: var(--cred-bg); }
  .credentialing .band { background: var(--cred-band); }
  .contact-us { top: 927px; background: var(--contact-bg); }
  .contact-us .band { background: var(--contact-band); }
</style>
</head>
<body>
  <main class="flier">
    <header class="header">
      <div class="brand"><span class="brand-dot"></span>VEGA BILLING</div>
      <span class="contact-rule"></span>
      <address class="contact" style="font-style:normal">
        Company Office Address<br>
        Pohne No: 000 111 222<br>
        Email : your@emailaddress
      </address>
    </header>

    <section class="section billing">
      <div class="band"><h2 class="label">MEDICAL BILLING</h2></div>
      <p class="copy">Would you prefer to spend time focusing on your clients and running your practice rather than trying to stay up to speed with the constantly changing medical billing rules and regulations? Let us help you by managing your medical billing and dealing with the insurance companies on your behalf! We work with you to tailor the entire medical billing process to suit your practices needs while making it as smooth and painless as possible.</p>
    </section>

    <section class="section aging">
      <div class="band"><h2 class="label">AGING</h2></div>
      <p class="copy">Are you leaving money on the table? Are you able to do the follow-through needed to keep your aging in check and more money flowing into your practice? Are you uncertain about how to get insurance to pay on claims that should be covered but for some reason they decided not to? We can clean up your aging, reduce the amount of time it takes for claims to pay out, and we can keep your aging to a minimum.</p>
    </section>

    <section class="section credentialing">
      <div class="band"><h2 class="label">CREDENTIALING</h2></div>
      <p class="copy">Are you wanting to get contracted with insurance companies but aren’t sure how to go about it? Are you wanting to expand your client base by having the option to bill insurance? Let us take the confusion out of what can seem like a daunting task! We can get you and your practitioners contracted with the insurance companies of your choice and help you navigate through the process every step of the way!</p>
    </section>

    <section class="section contact-us">
      <div class="band"><h2 class="label">CONTACT US</h2></div>
      <p class="copy">If any of these processes are something you would like our help with or to consult with us on, please email us or give us a call! We specialize in billing and contracting for Nutritionists and Dietitians. We would love to help you expand your business and take the pain and frustration out of billing so you can focus on your clients.</p>
    </section>
  </main>
</body>
</html>
```